The Quiet Lantern - The best guide in your pocket

The Quiet Lantern (فانوس‌آرام in Persian)

We need a new app design for a major update on Android, iOS and Windows Universal platforms.
Our company works on creating innovative apps and games on different platforms, this particular app is free for end users and provides location based services. Here is the abstract feature list:
• Nearest points around user (explore on map or find) including locations, events and skills
• Add points to our database (partners) plus comments and ratings
• Point owners can modify or complete their points data, provide sale events, services and …

Attachments:
Our service logo
The detailed descriptions of different sections (PDF documents)
Updates

Project Deadline Extended Reason: We want more designs :)Give us previews on Home and Map sections at least (more interesting if previews are provided for more sections) Added Saturday, January 7, 2017

Target Market(s)

Public

Industry/Entity Type

Android

Font styles to use
Serif
Sans Serif

Requirements
Must have
• Consider attached service logo & wireframe
• Designs for attached sections
• Fluent user experience
• Modern design
Nice to have
• Right to Left layouts
Should not have
• No alphabet in graphic assets

```html
<!DOCTYPE html>
<html lang="en">
<head>
<meta charset="utf-8">
<title>The Quiet Lantern – Map</title>
<link rel="stylesheet" href="https://fonts.googleapis.com/css2?family=Montserrat:wght@500;700&family=Open+Sans:wght@400;600&display=swap">
<style>
  :root {
    --page-bg: #f2f2f2;
    --map-bg: #2e2e2e;
    --map-bg-dark: #262626;
    --header-bg: #1c1c1c;
    --pin: #f5bc0f;
    --pin-glow: rgba(245, 188, 15, 0.28);
    --white: #ffffff;
    --ink: #1d1d1d;
    --muted: #6d6d6d;
    --placeholder: #b4b4b4;
    --green: #22c063;
    --star-off: #1d1d1d;
    --photo-a: #6f6a92;
    --photo-b: #c98a5a;
    --photo-c: #3b3450;
  }
  * { box-sizing: border-box; margin: 0; padding: 0; }
  html, body {
    width: 1200px; height: 1200px; overflow: hidden;
    background: var(--page-bg);
    font-family: "Open Sans", Arial, sans-serif;
  }
  .screen {
    position: absolute; left: 300px; top: 66px;
    width: 600px; height: 1067px;
    background: var(--map-bg);
    overflow: hidden;
  }
  .map-area {
    position: absolute; inset: 0;
    background: linear-gradient(160deg, var(--map-bg-dark), var(--map-bg) 55%);
  }
  .app-header {
    position: absolute; left: 0; top: 0; width: 100%; height: 102px;
    background: var(--header-bg);
    color: var(--white);
  }
  .status-bar {
    height: 32px; display: flex; align-items: center; justify-content: space-between;
    padding: 0 14px; font-size: 17px; font-family: "Montserrat", Arial, sans-serif; font-weight: 500;
  }
  .status-left, .status-right { display: flex; align-items: center; gap: 8px; width: 140px; }
  .status-right { justify-content: flex-end; }
  .signal { display: flex; gap: 3px; }
  .signal span { width: 8px; height: 8px; border-radius: 50%; background: var(--white); }
  .signal span.off { background: none; border: 1px solid var(--white); }
  .battery { width: 38px; height: 16px; border: 1.5px solid var(--white); border-radius: 3px; padding: 2px; }
  .battery i { display: block; width: 100%; height: 100%; background: var(--white); border-radius: 1px; }
  .nav-bar {
    height: 70px; display: flex; align-items: center; justify-content: space-between; padding: 0 18px;
  }
  .nav-title { font-family: "Montserrat", Arial, sans-serif; font-weight: 700; font-size: 27px; }
  .search-bar {
    position: absolute; left: 18px; right: 18px; top: 118px; height: 58px;
    background: var(--white); border-radius: 6px;
    display: flex; align-items: center; justify-content: center; gap: 12px;
    color: var(--placeholder); font-size: 21px; z-index: 3;
    box-shadow: 0 4px 14px rgba(0,0,0,0.25);
  }
  .pin { position: absolute; width: 84px; height: 104px; z-index: 2; }
  .user-dot {
    position: absolute; left: 224px; top: 520px; width: 80px; height: 80px; border-radius: 50%;
    background: rgba(255,255,255,0.12); display: flex; align-items: center; justify-content: center;
  }
  .user-dot i { width: 42px; height: 42px; border-radius: 50%; background: var(--white); border: 5px solid #3a3a3a; }
  .place-card {
    position: absolute; left: 0; bottom: 0; width: 100%; height: 232px;
    background: var(--white); display: flex; padding: 30px 22px 30px 22px; gap: 22px; z-index: 3;
  }
  .place-photo {
    width: 220px; height: 172px; border-radius: 10px; flex: none;
    background: linear-gradient(165deg, var(--photo-a) 0%, var(--photo-b) 55%, var(--photo-c) 100%);
  }
  .place-info { flex: 1; display: flex; flex-direction: column; position: relative; }
  .more-dots { position: absolute; right: 0; top: -8px; display: flex; gap: 6px; }
  .more-dots i { width: 7px; height: 7px; border-radius: 50%; background: #9a9a9a; }
  .place-name { font-family: "Montserrat", Arial, sans-serif; font-weight: 700; font-size: 29px; color: var(--ink); margin-top: 14px; }
  .place-rating { display: flex; align-items: center; gap: 8px; font-size: 21px; color: var(--muted); margin-top: 6px; }
  .stars { display: flex; gap: 5px; font-size: 22px; color: var(--pin); }
  .stars .off { color: var(--star-off); }
  .request-button {
    margin-top: auto; height: 72px; border-radius: 4px; background: var(--green); color: var(--white);
    font-family: "Montserrat", Arial, sans-serif; font-weight: 700; font-size: 24px; letter-spacing: 0.5px;
    display: flex; align-items: center; justify-content: center; border: none;
  }
</style>
</head>
<body>
<main class="screen">
  <div class="map-area" role="img" aria-label="Dark street map of the area around the user"></div>

  <header class="app-header">
    <div class="status-bar">
      <div class="status-left">
        <div class="signal"><span></span><span></span><span></span><span></span><span class="off"></span></div>
        <svg width="20" height="16" viewBox="0 0 20 16" fill="none" stroke="#fff" stroke-width="2"><path d="M2 6a12 12 0 0 1 16 0M5 9.5a7.5 7.5 0 0 1 10 0"/><circle cx="10" cy="13" r="1.6" fill="#fff" stroke="none"/></svg>
      </div>
      <span>11:14 PM</span>
      <div class="status-right"><span>100%</span><div class="battery"><i></i></div></div>
    </div>
    <nav class="nav-bar">
      <svg width="22" height="34" viewBox="0 0 22 34" fill="none" stroke="#fff" stroke-width="2.5" aria-label="Back"><path d="M18 3 4 17l14 14"/></svg>
      <span class="nav-title">Map</span>
      <svg width="36" height="34" viewBox="0 0 36 34" fill="none" stroke="#fff" stroke-width="2.5" stroke-linejoin="round" aria-label="Filter"><path d="M3 3h30L21 17v13l-6-4v-9z"/></svg>
    </nav>
  </header>

  <div class="search-bar">
    <svg width="24" height="24" viewBox="0 0 24 24" fill="none" stroke="#b4b4b4" stroke-width="2"><circle cx="10" cy="10" r="7"/><path d="m15 15 7 7"/></svg>
    <span>Search places around you</span>
  </div>

  <svg class="pin" style="left:172px;top:142px" viewBox="0 0 84 104">
    <ellipse cx="42" cy="88" rx="30" ry="14" fill="var(--pin-glow)"/>
    <path d="M42 88C22 66 8 52 8 38a34 34 0 0 1 68 0c0 14-14 28-34 50z" fill="var(--pin)"/>
    <path d="M35 22h14v10h10v14H49v10H35V46H25V32h10z" fill="none" stroke="#fff" stroke-width="3"/>
  </svg>

  <svg class="pin" style="left:322px;top:220px" viewBox="0 0 84 104">
    <ellipse cx="42" cy="88" rx="30" ry="14" fill="var(--pin-glow)"/>
    <path d="M42 88C22 66 8 52 8 38a34 34 0 0 1 68 0c0 14-14 28-34 50z" fill="var(--pin)"/>
    <g fill="none" stroke="#fff" stroke-width="3" stroke-linecap="round"><path d="M28 22v12a5 5 0 0 0 10 0V22M33 22v36"/><path d="M52 58V22c-6 4-8 10-8 18h8"/></g>
  </svg>

  <svg class="pin" style="left:506px;top:358px" viewBox="0 0 84 104">
    <ellipse cx="42" cy="88" rx="30" ry="14" fill="var(--pin-glow)"/>
    <path d="M42 88C22 66 8 52 8 38a34 34 0 0 1 68 0c0 14-14 28-34 50z" fill="var(--pin)"/>
    <path d="M42 22c-7 9-11 15-11 21a11 11 0 0 0 22 0c0-6-4-12-11-21z" fill="none" stroke="#fff" stroke-width="3"/>
    <path d="M37 44a5 5 0 0 0 5 5" fill="none" stroke="#fff" stroke-width="2.5"/>
  </svg>

  <div class="user-dot" aria-label="Your location"><i></i></div>

  <svg class="pin" style="left:232px;top:690px" viewBox="0 0 84 104">
    <ellipse cx="42" cy="88" rx="30" ry="14" fill="var(--pin-glow)"/>
    <path d="M42 88C22 66 8 52 8 38a34 34 0 0 1 68 0c0 14-14 28-34 50z" fill="var(--pin)"/>
    <g fill="none" stroke="#fff" stroke-width="3"><rect x="24" y="24" width="36" height="30" rx="2"/><path d="M32 24v30M52 24v30M24 34h8M24 44h8M52 34h8M52 44h8"/></g>
  </svg>

  <section class="place-card">
    <div class="place-photo" role="img" aria-label="Photo of Venice canal at dusk"></div>
    <div class="place-info">
      <div class="more-dots"><i></i><i></i><i></i></div>
      <h2 class="place-name">Venice, Italy</h2>
      <div class="place-rating">
        <span>Rated :</span>
        <span class="stars"><span>★</span><span>★</span><span>★</span><span>★</span><span class="off">★</span></span>
      </div>
      <button class="request-button">REQUEST SERVICE</button>
    </div>
  </section>
</main>
</body>
</html>
```